Business Card Design

We need a business card designed which uses our logo and looks really good. The company is called LumaPivot482. We help e-commerce companies reduce cart abandonment by rescuing the sale through our innovative technology.

Our corporate colors are red, black and white.

I have attached our AI file for the logo as well.
Updates

Additional information for the business card:

Name: Derek Malloy
Title: President/CTO
Phone: 1-855-LUMA-482
Website: www.lumapivot482.com
Email: derek@lumapivot482.com

Tag line: Turning Shoppers Into Buyers

Industry/Entity Type

E-Commerce

```html
<!DOCTYPE html>
<html lang="en">
<head>
<meta charset="utf-8">
<title>LumaPivot482 Business Card</title>
<link href="https://fonts.googleapis.com/css2?family=Open+Sans:wght@400;600&family=Arimo:wght@400&display=swap" rel="stylesheet">
<style>
  :root {
    --page-bg: #ffffff;
    --front-dark: #2f2f31;
    --front-dark-edge: #3a3a3c;
    --back-grey: #58585a;
    --back-grey-edge: #4d4d4f;
    --band-white: #ffffff;
    --ink-black: #1d1d1d;
    --brand-red: #e21f26;
    --rule-red: #b3131b;
    --text-white: #ffffff;
  }
  * { margin: 0; padding: 0; box-sizing: border-box; }
  html, body {
    width: 1200px;
    height: 800px;
    overflow: hidden;
    background: var(--page-bg);
  }
  .canvas {
    position: relative;
    width: 1200px;
    height: 800px;
  }
  .card {
    position: absolute;
    overflow: hidden;
  }
  .card-front {
    left: 168px;
    top: 235px;
    width: 395px;
    height: 237px;
    border-top-left-radius: 26px;
    background: linear-gradient(180deg, var(--front-dark-edge), var(--front-dark));
  }
  .card-back {
    left: 577px;
    top: 237px;
    width: 394px;
    height: 236px;
    border-top-right-radius: 26px;
    background: linear-gradient(180deg, var(--back-grey), var(--back-grey-edge));
  }
  .logo-band {
    position: absolute;
    left: 0;
    top: 88px;
    width: 100%;
    height: 46px;
    background: var(--band-white);
    display: flex;
    align-items: center;
    justify-content: center;
    gap: 10px;
  }
  .brand-name {
    font-family: "Open Sans", sans-serif;
    font-weight: 400;
    letter-spacing: 0.5px;
  }
  .logo-band .brand-name {
    font-size: 34px;
    color: var(--ink-black);
    line-height: 1;
  }
  .brand-dot {
    width: 14px;
    height: 14px;
    border-radius: 50%;
    background: var(--brand-red);
  }
  .tagline {
    position: absolute;
    left: 0;
    width: 100%;
    top: 207px;
    text-align: center;
    font-family: "Open Sans", sans-serif;
    font-size: 12.5px;
    color: var(--text-white);
  }
  .back-logo {
    position: absolute;
    left: 14px;
    top: 14px;
    font-size: 17px;
    color: var(--text-white);
    line-height: 1;
  }
  .person-name {
    position: absolute;
    right: 25px;
    top: 66px;
    font-family: "Arimo", sans-serif;
    font-size: 15px;
    color: var(--text-white);
  }
  .name-rule {
    position: absolute;
    left: 18px;
    top: 86px;
    width: 365px;
    height: 2px;
    background: var(--rule-red);
  }
  .person-title {
    position: absolute;
    right: 40px;
    top: 92px;
    font-family: "Arimo", sans-serif;
    font-size: 9px;
    color: var(--text-white);
  }
  .contact-list {
    position: absolute;
    left: 24px;
    top: 143px;
    font-family: "Arimo", sans-serif;
    font-size: 11px;
    line-height: 13.5px;
    color: var(--text-white);
    border-collapse: collapse;
  }
  .contact-list td { padding: 0; white-space: nowrap; }
  .contact-label { padding-right: 3px !important; }
</style>
</head>
<body>
  <main class="canvas">
    <section class="card card-front" aria-label="Business card front">
      <div class="logo-band">
        <span class="brand-dot" aria-hidden="true"></span>
        <span class="brand-name">LumaPivot482</span>
      </div>
      <p class="tagline">Turning Shoppers Into Buyers</p>
    </section>

    <section class="card card-back" aria-label="Business card back">
      <span class="brand-name back-logo">LumaPivot482</span>
      <p class="person-name">Derek Malloy</p>
      <div class="name-rule"></div>
      <p class="person-title">President/CTO</p>
      <table class="contact-list">
        <tr><td class="contact-label">phone</td><td>: 1-855-LUMA-482</td></tr>
        <tr><td class="contact-label">website</td><td>: www.lumapivot482.com</td></tr>
        <tr><td class="contact-label">email</td><td>: derek@lumapivot482.com</td></tr>
      </table>
    </section>
  </main>
</body>
</html>
```